Aircraft maintenance buisness card

I am an aircraft mechanic looking for a personal buisness card . I would like my name and a title of Aircraft Maintenance Manager . I would like a suttle picture of an aircraft and helicopter .

elegant and professional wtih my contact .

My name should be on the car and Aircraft Maintenance Manager under with my contact infor below .

i have attached some pictures but i am open to other pics and ideas . I would like a airliner or private jet and a helicopter in the picture . The Images should be suttle and not the main idea . I also uploaded a picture of a jet engine which is cool . Be creative and i will work with you to finalize something .
Updates

Project Deadline Extended
Reason: Looking for more variations . Very good so far but looiking for a bit more styles and i uploaded my logo that i purchased . Please use my logo and be creative with it . I like some variations of black card with maybe some pictures that i uploaded but i am open to ideas . Be creative and i will work with you .

Project Deadline Extended
Reason: Looking for more designs and variations . Not yet satisfied with the designs i have gotten .

Industry/Entity Type

Aviation

Contact Information for Business Card

Aircraft Maintenance Manager

Font styles to use
Serif

Colors

Designer to choose colors to be used in the design.

Requirements
Must have
• An aviation related Logo if possible incorporated in the card possibly
• My name
• Tobias Marven Ellery
• 482 Pellow Ave.
• Kearny , NJ
• 07519
• Email: Tmskyworks@quillmail.net
Nice to have
• Suttle Backround of a Private Jet or Airliner and a Helicopter .

```html
<!DOCTYPE html>
<html lang="en">
<head>
<meta charset="utf-8">
<title>Tobias Marven Ellery – Business Card</title>
<link rel="stylesheet" href="https://fonts.googleapis.com/css2?family=Cinzel:wght@400;600&family=Jost:wght@400;600&display=swap">
<style>
  :root {
    --page: #2a2a2c;
    --card: #232325;
    --card-edge: #3a3a3d;
    --pattern-a: #2b2b2e;
    --pattern-b: #1f1f21;
    --emboss: #141415;
    --emboss-light: #5a5a5e;
    --blue: #2f5fc4;
    --text: #f2f2f2;
  }
  * { margin: 0; padding: 0; box-sizing: border-box; }
  html, body { width: 1200px; height: 900px; overflow: hidden; }
  body {
    background: var(--page);
    display: flex;
    flex-direction: column;
    align-items: center;
    justify-content: center;
    gap: 40px;
  }
  .card {
    position: relative;
    width: 700px;
    height: 400px;
    background: var(--card);
    border: 1px solid var(--card-edge);
    box-shadow: 0 12px 30px rgba(0,0,0,.45);
    overflow: hidden;
  }
  /* Front */
  .card-front .pattern {
    position: absolute;
    inset: 0;
    background: radial-gradient(circle at 50% 45%, var(--pattern-a), var(--pattern-b));
  }
  .card-front .identity {
    position: absolute;
    inset: 0;
    display: flex;
    flex-direction: column;
    align-items: center;
    justify-content: center;
    text-align: center;
  }
  .card-front .name {
    font-family: "Cinzel", serif;
    font-weight: 400;
    font-size: 36px;
    letter-spacing: 1.5px;
    color: var(--emboss);
    text-shadow: 0 1px 0 var(--emboss-light);
  }
  .card-front .title {
    margin-top: 4px;
    font-family: "Cinzel", serif;
    font-size: 17px;
    letter-spacing: 1px;
    color: var(--emboss);
    text-shadow: 0 1px 0 var(--emboss-light);
  }
  /* Back */
  .card-back { font-family: "Jost", sans-serif; color: var(--text); }
  .brand {
    position: absolute;
    top: 60px;
    right: 50px;
    display: flex;
    align-items: center;
    gap: 12px;
  }
  .brand-mark { width: 44px; height: 44px; background: var(--blue); border-radius: 6px; }
  .brand-name {
    font-weight: 600;
    font-size: 22px;
    letter-spacing: 2px;
    color: var(--blue);
  }
  .holder { position: absolute; left: 50px; top: 148px; }
  .holder .name {
    font-weight: 600;
    font-size: 26px;
    letter-spacing: .5px;
    text-transform: uppercase;
    color: var(--blue);
  }
  .holder .title { font-size: 19px; letter-spacing: 1px; margin-top: 2px; font-weight: 400; }
  .divider {
    position: absolute;
    left: 50px;
    right: 50px;
    top: 224px;
    height: 1px;
    background: var(--blue);
  }
  .contact {
    position: absolute;
    left: 50px;
    top: 244px;
    list-style: none;
    font-size: 19px;
    line-height: 1.45;
    letter-spacing: .5px;
  }
  .address {
    position: absolute;
    right: 50px;
    bottom: 34px;
    text-align: right;
    font-size: 20px;
    line-height: 1.3;
    letter-spacing: .5px;
    font-style: normal;
  }
  .address .label { color: var(--blue); }
</style>
</head>
<body>
  <section class="card card-front">
    <div class="pattern" role="img" aria-label="Faint repeating pattern of small aircraft silhouettes"></div>
    <div class="identity">
      <h1 class="name">Tobias Marven Ellery</h1>
      <p class="title">Aircraft Maintenance Manager</p>
    </div>
  </section>

  <section class="card card-back">
    <div class="brand">
      <span class="brand-mark"></span>
      <span class="brand-name">MARVEN AVIATION</span>
    </div>
    <div class="holder">
      <h2 class="name">Tobias Marven Ellery</h2>
      <p class="title">Aircraft Maintenance Manager</p>
    </div>
    <div class="divider"></div>
    <ul class="contact">
      <li>Tel: 555-014-8823</li>
      <li>Email: tobias@marvenaviation.com</li>
      <li>Web: marvenaviation.com</li>
    </ul>
    <address class="address">
      <span class="label">Address:</span><br>
      482 Pellow Ave.<br>
      Brookvale, OH, 07519
    </address>
  </section>
</body>
</html>
```